Geschäftspapiere für gemeinnützige Organisation im weltweiten Bildungsbereich
Zielgruppe
Wir sind eine gemeinnützige Organisation mit Projekten im Bildungsbereich weltweit. Unsere Zielgruppe sind andere gemeinnützige Organisationen und Studenten.
Aufgabenstellung
Das Logo sollte aud das Geschäftspapier sowie änhnliche Farben bei den Informationen genutzt werden (orange und/ oder grün).
KLT Berlin gemeinnützige GmbH
Falkenhainer Weg 14, D-12489 Berlin
www.klt-bildung.example I Geschäftsführer: Jorinde Paskova, Lukas Drömberg I Amtsgericht Berlin-Charlottenburg, HRB 417592 B

```html
<!DOCTYPE html>
<html lang="de">
<head>
<meta charset="utf-8">
<title>KLT Berlin – Briefbogen</title>
<link href="https://fonts.googleapis.com/css2?family=Arimo&family=Lato:wght@400;700&display=swap" rel="stylesheet">
<style>
  :root {
    --bg: #f1efed;
    --paper: #ffffff;
    --band-light: #fbb977;
    --band-orange: #f7941d;
    --band-green: #acd136;
    --accent: #e8762c;
    --text: #111111;
    --muted: #555555;
    --footer: #8a8a8a;
  }
  html, body {
    margin: 0;
    width: 1200px;
    height: 3000px;
    overflow: hidden;
    background: var(--bg);
  }
  .letterhead {
    position: absolute;
    left: 100px;
    top: 790px;
    width: 1000px;
    height: 1417px;
    background: var(--paper);
    box-shadow: 0 3px 14px rgba(0,0,0,0.12);
    font-family: "Lato", sans-serif;
  }
  .side-band { position: absolute; left: 0; width: 57px; }
  .side-band--light { top: 0; height: 471px; background: var(--band-light); }
  .side-band--orange { top: 471px; height: 236px; background: var(--band-orange); }
  .side-band--green { top: 707px; height: 236px; background: var(--band-green); }

  .brand {
    position: absolute;
    left: 105px;
    top: 110px;
    display: flex;
    align-items: center;
    gap: 16px;
  }
  .brand__dot {
    width: 34px; height: 34px;
    border-radius: 50%;
    background: var(--band-orange);
  }
  .brand__name {
    font-family: "Lato", sans-serif;
    font-weight: 700;
    font-size: 46px;
    letter-spacing: 2px;
    color: var(--accent);
  }

  .sender {
    position: absolute;
    right: 72px;
    top: 160px;
    text-align: right;
    font-size: 21px;
    line-height: 25px;
  }
  .sender__name { color: var(--accent); }
  .sender__address { color: var(--muted); }

  .memo {
    position: absolute;
    left: 105px;
    top: 278px;
    font-size: 17.5px;
    line-height: 25.5px;
    color: var(--text);
    border-collapse: collapse;
  }
  .memo th { text-align: left; font-weight: 700; padding: 0 18px 0 0; }
  .memo td { padding: 0; }

  .body-text {
    position: absolute;
    left: 107px;
    top: 478px;
    width: 787px;
    font-family: "Arimo", sans-serif;
    font-size: 18.5px;
    line-height: 22px;
    color: var(--text);
    text-align: justify;
  }
  .body-text p { margin: 0 0 22px; }

  .footer {
    position: absolute;
    left: 0; right: 0;
    top: 1346px;
    text-align: center;
    font-size: 16.5px;
    color: var(--footer);
  }
  .footer__sep { color: var(--band-green); padding: 0 3px; }
</style>
</head>
<body>
  <main class="letterhead">
    <div class="side-band side-band--light"></div>
    <div class="side-band side-band--orange"></div>
    <div class="side-band side-band--green"></div>

    <div class="brand">
      <span class="brand__dot"></span>
      <span class="brand__name">KLT BERLIN</span>
    </div>

    <div class="sender">
      <div class="sender__name">KLT Berlin gemeinnützige GmbH</div>
      <div class="sender__address">Falkenhainer Weg 14, D-12489 Berlin</div>
    </div>

    <table class="memo">
      <tr><th>To:</th><td>[Recepient Name]</td></tr>
      <tr><th>From:</th><td>[Your Name]</td></tr>
      <tr><th>Cc:</th><td>[Name]</td></tr>
      <tr><th>Date:</th><td>[Date]</td></tr>
      <tr><th>Re:</th><td>[Subject]</td></tr>
    </table>

    <div class="body-text">
      <p>Lorem ipsum dolor sit amet, consectetur adipiscing elit, sed do eiusmod tempor incididunt ut labore et dolore magna aliqua. Proin sagittis nisl rhoncus mattis rhoncus urna neque viverra. Sed vulputate odio ut enim blandit volutpat maecenas. Turpis in eu mi bibendum neque. Faucibus turpis in eu mi bibendum neque egestas. Massa vitae tortor condimentum lacinia quis vel eros donec. Erat pellentesque adipiscing commodo elit at imperdiet dui accumsan. Ullamcorper velit sed ullamcorper morbi. Vel facilisis volutpat est velit egestas dui. Sed lectus vestibulum mattis ullamcorper velit sed ullamcorper. Vestibulum morbi blandit cursus risus at ultrices mi tempus. Elit duis tristique sollicitudin nibh sit amet commodo nulla facilisi. Suspendisse interdum consectetur libero id. Sapien et ligula ullamcorper malesuada proin libero nunc consequat interdum. Sed vulputate odio ut enim blandit volutpat maecenas volutpat. Quis enim lobortis scelerisque fermentum dui.</p>
      <p>Praesent elementum facilisis leo vel. Enim facilisis gravida neque convallis a. Gravida arcu ac tortor dignissim convallis aenean et tortor at. Magna ac placerat vestibulum lectus mauris ultrices eros in. Bibendum est ultricies integer quis auctor elit. Odio morbi quis commodo odio aenean. Dolor sed viverra ipsum nunc aliquet bibendum enim facilisis. Iaculis urna id volutpat lacus laoreet. Posuere ac ut consequat semper viverra nam libero justo laoreet. Odio pellentesque diam volutpat commodo sed egestas egestas fringilla.</p>
      <p>Non arcu risus quis varius quam quisque id diam vel. Nunc scelerisque viverra mauris in aliquam sem fringilla. Vitae proin sagittis nisl rhoncus mattis. Pretium quam vulputate dignissim suspendisse in est ante. Sit amet est placerat in egestas erat imperdiet sed euismod. Dui ut ornare lectus sit amet est placerat in egestas. Diam phasellus vestibulum lorem sed risus ultricies tristique. In fermentum et sollicitudin ac. Blandit massa enim nec dui nunc mattis enim ut tellus. Egestas fringilla phasellus faucibus scelerisque eleifend donec pretium vulputate. Penatibus et magnis dis parturient montes.</p>
    </div>

    <footer class="footer">
      www.klt-bildung.example<span class="footer__sep">|</span>Geschäftsführer: Jorinde Paskova, Lukas Drömberg<span class="footer__sep">|</span>Amtsgericht Berlin-Charlottenburg, HRB 417592 B
    </footer>
  </main>
</body>
</html>
```